Softwareentwickler sucht Disigne für Flyer
Zielgruppe
Softwareentwicklung im Bereich Feuerwehr und Rettungsdienst.
Aufgabenstellung
Ich benötige für unsere Software ein Flyer für ein Messeauftritt. Wir haben eine Homepage (www.norvaplex.de) ,wo unsere Software beschrieben wird. Es besteht bereits ein Softwarelogo (Norvaplex) welches auch auf unserer Hompage zu sehen ist.

```html
<!DOCTYPE html>
<html lang="de">
<head>
<meta charset="utf-8">
<title>Norvaplex Flyer</title>
<link href="https://fonts.googleapis.com/css2?family=Oswald:wght@300;400;600&display=swap" rel="stylesheet">
<style>
  :root {
    --green: #3f9e25;
    --green-mid: #4fae30;
    --green-light: #a9d493;
    --paper: #ffffff;
    --paper-soft: #f3f3f3;
    --backdrop: #d9d9d8;
    --photo-dark: #3c3f42;
    --photo-light: #e8eaeb;
  }
  * { box-sizing: border-box; margin: 0; padding: 0; }
  html, body { width: 1200px; height: 800px; overflow: hidden; }
  body {
    background: var(--backdrop);
    font-family: "Oswald", "Arial Narrow", sans-serif;
    color: var(--green);
    text-transform: uppercase;
  }
  .brochure {
    position: absolute; left: 63px; top: 20px;
    width: 1074px; height: 760px;
    display: flex;
    box-shadow: 0 6px 24px rgba(0,0,0,.18);
  }
  .panel { position: relative; width: 358px; height: 760px; background: var(--paper); overflow: hidden; }
  .panel--middle { background: var(--paper-soft); }

  .brand {
    position: absolute; top: 52px; left: 0; right: 0;
    display: flex; align-items: center; justify-content: center; gap: 10px;
    font-weight: 600; font-size: 28px; line-height: 1; color: var(--green);
  }
  .brand__square { width: 14px; height: 14px; background: var(--green); }

  .band {
    position: absolute; left: 0; right: 0; top: 118px; height: 60px;
    background: var(--green); color: var(--paper); text-align: center;
    line-height: 1.05; padding-top: 8px;
  }
  .band__main { font-weight: 600; font-size: 22px; display: block; }
  .band__sub { font-weight: 300; font-size: 20px; display: block; }

  .block { position: absolute; }
  .block--green { background: var(--green-mid); color: var(--paper); }
  .block--light { background: var(--green-light); color: var(--paper); }
  .photo { position: absolute; }

  .statement {
    display: flex; align-items: center; justify-content: center; text-align: center;
    font-weight: 300; font-size: 21px; line-height: 1.25;
  }
  .note {
    display: flex; align-items: center; justify-content: center; text-align: center;
    font-weight: 300; font-size: 10.5px; line-height: 1.45; padding: 12px;
  }

  .body-text {
    position: absolute; left: 22px; right: 22px;
    text-align: center; font-size: 10.5px; line-height: 1.4; font-weight: 400;
  }
  .body-text p + p { margin-top: 12px; }
  .body-text strong { font-weight: 600; }

  .offer-title {
    position: absolute; top: 60px; left: 0; right: 0; text-align: center; line-height: 1.05;
  }
  .offer-title__main { display: block; font-weight: 600; font-size: 22px; }
  .offer-title__sub { display: block; font-weight: 300; font-size: 20px; }
  .offer-list {
    position: absolute; top: 126px; left: 45px; right: 45px;
    list-style: none; text-align: center; font-size: 10.5px; line-height: 1.6;
  }
  .offer-list li::before { content: "• "; }

  .footer-square {
    position: absolute; left: 124px; bottom: 0; width: 110px; height: 96px;
    background: var(--green-mid);
    display: flex; align-items: center; justify-content: center;
  }
</style>
</head>
<body>
<main class="brochure">

  <section class="panel panel--left">
    <div class="brand"><span class="brand__square"></span>Norvaplex</div>
    <div class="band"><span class="band__main">Lagerverwaltung</span><span class="band__sub">mit Norvaplex</span></div>
    <div class="block block--green statement" style="left:22px; top:200px; width:150px; height:300px;">
      In der<br>Lagerver-<br>waltung<br>Barcode-<br>Systeme<br>einsetzen
    </div>
    <div class="photo" role="img" aria-label="Foto eines schwarzen Handscanners auf hellem Untergrund"
         style="left:172px; top:190px; width:186px; height:160px; background:linear-gradient(160deg,var(--photo-light) 30%,#b9bcbe 60%,var(--photo-dark) 75%,var(--photo-light) 90%);"></div>
    <div class="block block--light note" style="left:172px; top:350px; width:186px; height:140px;">
      Per Scanner verbuchen Sie Ein- und Ausgänge im Lager schnell und einfach. Im Folgenden können die Bestände ganz unkompliziert verwaltet werden.
    </div>
    <div class="body-text" style="top:520px;">
      <p>Zur übersichtlicheren Erfassung von Waren in der Lagerverwaltung können Barcode-Systeme eine erhebliche Erleichterung darstellen.</p>
      <p>Um diese Prozesse für Ihre Mitarbeiter einfacher zu gestalten, können Sie in Ihrer Lagerverwaltung Barcode-Systeme einsetzen. Für die Inventarisierung aller Artikel benötigen Sie Barcode-Etiketten, mit denen Sie die Produkte bzw. Ihre Regale bekleben.</p>
      <p>Das softwarebasierte System Norvaplex ermöglicht die Abbildung des vollständigen innerbetrieblichen Materialflusses zur unternehmerischen Verwaltung von Lagerbeständen.</p>
    </div>
  </section>

  <section class="panel panel--middle">
    <h2 class="offer-title"><span class="offer-title__main">Folgendes bieten</span><span class="offer-title__sub">wir Ihnen derzeit an!</span></h2>
    <ul class="offer-list">
      <li>Materialverwaltung</li>
      <li>Steuerung von Benutzerkonten</li>
      <li>Verwaltung von Lieferanten und Lagerstandorten</li>
      <li>Mindesthaltbarkeitskontrolle</li>
      <li>Temperaturüberwachung von medizinischen Kühlschränken mit SMS Alarm</li>
      <li>Live Streaming von Scanaktivität über Monitor in Ihrem Lager</li>
      <li>Komplettes Bestellwesen inkl. Ein- und Auslagerungsmöglichkeiten</li>
      <li>Inventur und Artikelstatistiken</li>
      <li>MPG Geräteverwaltung mit E-Mail Erinnerungen</li>
      <li>Fuhrparkmanagment</li>
      <li>Support</li>
    </ul>
    <div class="photo" role="img" aria-label="Bildschirmansicht der Software mit grünen Menüschaltflächen"
         style="left:60px; top:470px; width:238px; height:150px; background:linear-gradient(180deg,#cfe6c3,#f3f3f3);"></div>
    <div class="footer-square">
      <svg width="54" height="54" viewBox="0 0 54 54" aria-hidden="true">
        <path d="M19 4h16v15h15v16H35v15H19V35H4V19h15z" fill="#ffffff"/>
      </svg>
    </div>
  </section>

  <section class="panel panel--right">
    <div class="brand"><span class="brand__square"></span>Norvaplex</div>
    <div class="band"><span class="band__main">Spezielle Features</span><span class="band__sub">in Norvaplex</span></div>
    <div class="photo" role="img" aria-label="Foto einer weißen Tastatur mit grünen Funktionstasten"
         style="left:0; top:190px; width:220px; height:260px; background:linear-gradient(150deg,#f6f6f6,#d4d6d7 70%,#9fc98a);"></div>
    <div class="block block--light note" style="left:18px; top:200px; width:150px; height:100px; font-size:10px;">
      Bei uns wird nur in Rechnung gestellt, was der Kunde wirklich nutzen möchte!
    </div>
    <div class="block block--green statement" style="left:190px; top:178px; width:168px; height:248px;">
      Modulare<br>Systeme<br>in der<br>Lagerver-<br>waltung
    </div>
    <div class="body-text" style="top:475px;">
      <p>Unsere Software ist modular aufgebaut, so dass einzeln Module gebucht werden können.</p>
      <p>Als Grundmodul bieten wir unsere Plattform Norvaplex Lagerverwaltung an, worauf sich alle weiteren Module aufbauen lassen.</p>
      <p><strong>Im Einzelnen sind dies:</strong><br>• Temperatur-Modul<br>• MPV-Modul (Medizinische Produkte Verwaltung nach MPG)<br>• Fuhrpark-Modul</p>
    </div>
  </section>

</main>
</body>
</html>
```